Vex Lira

Hello - our company Orbana 9 develops novel products for the skin, & hair care industry as well as dietary supplements. We're looking for a label design for a new product. The product is a premium hair loss/growth supplement. Our primary demo is women ages 45-65. I attached the brand logo & some competitive product designs that we find attractive.

I've been traveling & have not had the time to adequately review the designs, please be patient with me.

```html
<!DOCTYPE html>
<html lang="en">
<head>
<meta charset="utf-8">
<title>Vex Lira – Label</title>
<link rel="stylesheet" href="https://fonts.googleapis.com/css2?family=Exo+2:wght@400;500;600&display=swap">
<style>
  :root {
    --page: #eceff2;
    --label: #ffffff;
    --pattern-a: #f7f9fb;
    --pattern-b: #eef3f7;
    --slate: #7d8894;
    --blue: #3f93d4;
    --pill: #c4dcef;
    --pill-text: #ffffff;
  }
  * { margin: 0; padding: 0; box-sizing: border-box; }
  html, body {
    width: 1200px;
    height: 675px;
    overflow: hidden;
    background: var(--page);
    font-family: "Exo 2", sans-serif;
  }
  .canvas {
    position: relative;
    width: 1200px;
    height: 675px;
    display: flex;
    align-items: center;
    justify-content: center;
  }
  .label {
    position: relative;
    width: 760px;
    height: 600px;
    background: var(--label);
    border-radius: 6px;
    box-shadow: 0 2px 14px rgba(60, 80, 100, 0.08);
    overflow: hidden;
  }
  .label-pattern {
    position: absolute;
    inset: 0;
    background: radial-gradient(ellipse at 30% 35%, var(--pattern-a), var(--pattern-b));
  }
  .label-content {
    position: relative;
    height: 100%;
    display: flex;
    flex-direction: column;
    align-items: center;
    text-align: center;
    padding-top: 58px;
  }
  .maker-name {
    font-size: 30px;
    font-weight: 500;
    letter-spacing: 1px;
    color: var(--slate);
  }
  .maker-claim {
    margin-top: 10px;
    font-size: 11px;
    font-weight: 600;
    letter-spacing: 1.6px;
    color: var(--slate);
  }
  .ingredient-pill {
    margin-top: 58px;
    display: flex;
    align-items: center;
    gap: 14px;
    padding: 7px 18px;
    background: var(--pill);
    border-radius: 8px;
    color: var(--pill-text);
    font-size: 15px;
    font-weight: 600;
    letter-spacing: 1.5px;
  }
  .ingredient-pill .divider {
    width: 1px;
    height: 20px;
    background: var(--pill-text);
  }
  .ingredient-pill .ratio { font-size: 13px; }
  .product-name {
    margin-top: 40px;
    font-size: 72px;
    font-weight: 500;
    letter-spacing: 5px;
    color: var(--slate);
  }
  .strength {
    margin-top: 44px;
    font-size: 16px;
    font-weight: 600;
    letter-spacing: 1.4px;
    color: var(--slate);
  }
  .strength .accent { color: var(--blue); }
  .formula {
    margin-top: 66px;
    font-size: 12px;
    font-weight: 500;
    letter-spacing: 1.4px;
    color: var(--slate);
  }
  .audience {
    font-size: 30px;
    font-weight: 600;
    letter-spacing: 1.5px;
    color: var(--slate);
    line-height: 1.1;
  }
</style>
</head>
<body>
  <main class="canvas">
    <section class="label">
      <div class="label-pattern" role="img" aria-label="Faint light-blue network pattern of dots joined by thin lines"></div>
      <div class="label-content">
        <p class="maker-name">ORBANA 9</p>
        <p class="maker-claim">MEDICALLY PROVEN</p>
        <p class="ingredient-pill"><span>HE SHOU WU</span><span class="divider"></span><span class="ratio">12:1</span></p>
        <h1 class="product-name">VEX LIRA</h1>
        <p class="strength"><span class="accent">CLINICAL</span> STRENGTH</p>
        <p class="formula">ADVANCED FORMULA</p>
        <p class="audience">WOMEN</p>
      </div>
    </section>
  </main>
</body>
</html>
```